Corvale Motorized Shade Business Card

Hello, we've had our logo made. Now we are looking for a clean and cool looking business card. One side can just be the logo with any design elements that might look good with it. The other side will be Name, Phone Number and Email. There will not be an address on the card.

```html
<!DOCTYPE html>
<html lang="en">
<head>
<meta charset="utf-8">
<title>Corvale Motorized Shade – Business Card</title>
<link rel="stylesheet" href="https://fonts.googleapis.com/css2?family=Oswald:wght@600&family=Roboto:wght@400&display=swap">
<style>
  :root{
    --bg:#1e1e1f;
    --navy:#00396f;
    --blue-deep:#004a8c;
    --blue-sky:#03aeef;
    --sun:#fdc113;
    --ink:#1d1d1d;
    --rule:#b9b9b9;
    --white:#ffffff;
  }
  *{box-sizing:border-box;margin:0;padding:0}
  html,body{width:1200px;height:1015px;overflow:hidden;background:var(--bg)}
  .canvas{position:relative;width:1200px;height:1015px}

  .card{position:absolute;width:620px;height:354px;overflow:hidden;box-shadow:0 14px 30px rgba(0,0,0,.55)}

  /* Front */
  .card--front{left:80px;top:90px;
    background:linear-gradient(200deg,var(--blue-sky) 0%,#0288d6 38%,var(--blue-deep) 70%,var(--navy) 100%)}
  .card--front .streaks{position:absolute;inset:0}
  .wordmark{position:absolute;left:0;right:0;top:50%;transform:translateY(-50%);
    display:flex;align-items:center;justify-content:center;gap:14px}
  .wordmark__mark{width:22px;height:22px;background:var(--sun)}
  .wordmark__name{font-family:"Oswald",sans-serif;font-weight:600;font-size:34px;letter-spacing:1px;
    text-transform:uppercase;color:var(--white)}

  /* Back */
  .card--back{left:500px;top:560px;background:var(--white)}
  .card--back .wordmark{left:24px;right:auto;width:300px;top:160px;transform:none;justify-content:flex-start;gap:10px}
  .card--back .wordmark__mark{width:18px;height:18px}
  .card--back .wordmark__name{color:var(--navy);font-size:22px}
  .divider{position:absolute;left:330px;top:84px;width:1px;height:150px;background:var(--rule)}
  .contact{position:absolute;left:352px;top:92px}
  .contact__name{font-family:"Oswald",sans-serif;font-weight:600;font-size:24px;line-height:1;color:var(--navy);text-transform:uppercase}
  .contact__role{font-family:"Roboto",sans-serif;font-size:15px;color:var(--ink);margin-top:3px}
  .contact__list{list-style:none;margin-top:20px}
  .contact__list li{display:flex;align-items:center;gap:8px;font-family:"Roboto",sans-serif;font-size:14px;color:var(--ink);line-height:22px}
  .contact__list svg{width:15px;height:15px;flex:none}
  .bands{position:absolute;left:0;bottom:0;width:620px;height:80px}
</style>
</head>
<body>
<main class="canvas">

  <section class="card card--front" aria-label="Card front">
    <svg class="streaks" viewBox="0 0 620 354" preserveAspectRatio="none" aria-hidden="true">
      <polygon points="0,150 620,20 620,60 0,190" fill="#ffffff" opacity=".05"/>
      <polygon points="0,230 620,110 620,140 0,260" fill="#ffffff" opacity=".05"/>
      <polygon points="0,300 620,190 620,230 0,340" fill="#ffffff" opacity=".04"/>
    </svg>
    <div class="wordmark">
      <span class="wordmark__mark"></span>
      <span class="wordmark__name">Corvale Motorized Shade</span>
    </div>
  </section>

  <section class="card card--back" aria-label="Card back">
    <div class="wordmark">
      <span class="wordmark__mark"></span>
      <span class="wordmark__name">Corvale Motorized Shade</span>
    </div>
    <div class="divider"></div>
    <div class="contact">
      <p class="contact__name">Marcus Hale</p>
      <p class="contact__role">Managing Director</p>
      <ul class="contact__list">
        <li><svg viewBox="0 0 24 24" aria-hidden="true"><path fill="#00396f" d="M6.6 10.8a15.1 15.1 0 0 0 6.6 6.6l2.2-2.2c.3-.3.7-.4 1-.2 1.1.4 2.3.6 3.6.6.6 0 1 .4 1 1V20c0 .6-.4 1-1 1A17 17 0 0 1 3 4c0-.6.4-1 1-1h3.5c.6 0 1 .4 1 1 0 1.3.2 2.5.6 3.6.1.3 0 .7-.2 1z"/></svg>044-987 654 321</li>
        <li><svg viewBox="0 0 24 24" aria-hidden="true"><path fill="#00396f" d="M2 5h20v14H2z"/><path d="M2 5l10 8 10-8" fill="none" stroke="#fff" stroke-width="1.8"/></svg>info@corvaleshade.com</li>
        <li><svg viewBox="0 0 24 24" aria-hidden="true"><circle cx="12" cy="12" r="9.5" fill="none" stroke="#00396f" stroke-width="2"/><path d="M2.5 12h19M12 2.5c3 3 3 16 0 19M12 2.5c-3 3-3 16 0 19" fill="none" stroke="#00396f" stroke-width="1.6"/></svg>www.corvaleshade.com</li>
      </ul>
    </div>
    <svg class="bands" viewBox="0 0 620 80" preserveAspectRatio="none" aria-hidden="true">
      <polygon points="0,66 400,66 405,80 0,80" fill="var(--navy)"/>
      <polygon points="410,38 620,38 620,80 416,80" fill="var(--blue-sky)"/>
    </svg>
  </section>

</main>
</body>
</html>
```